Create and implement a Wordpress Template for a Blog/Podcast website

Hi, I need you to design and implement a WordPress theme into my website PathofthePlenty.com.
[login to view URL] is a blog/podcast about passive income education. The site is about educating people to think the way rich people think. The main purpose is to acquire financial freedom with Passive Income. Passive income is where you don't trade hours for dollars, but you get paid for the value you bring. Monthly cash flow is the main goal of passive income. Quitting your job and because you do not need to work for money is one of the main goals.
This site is for middle class people who want to quit their job and design their life how they want it to be if you didn't have to worry about their bills.
WordPress Theme Design
1. I have attached the logo for the site and the must be incorporated into the design well.
2. The site must be modern and inviting.
3. The font should be clean, simple, and easy to read. Include the domain name "[login to view URL]" Must be easy to read and distinguishable.
4. The design and artwork must be original and and have no copyright issues.
5. Even though the name has the word Rich in it, I don't want it to look fancy, flashy, gold, or opulent. No dollar signs, gold, or diamonds should be used. This is an educational site and is about the student learning, not the money.
Functionality of the site
1. Must have a static home page with the ability to place recent blog/podcast posts
2. Pages/Links would have Home, About, Blog, Start Here, Podcast, Ask Marvin, and Resources
3. Must have the ability for visitors to subscribe to the blog and future newsletters
Deliverable's must be installed onto the server and set up ready for launch. I want to be able to start posting blog/podcast entries as soon as the site is completed.

```html
<!DOCTYPE html>
<html lang="en">
<head>
<meta charset="utf-8">
<title>Path of the Plenty — Blog Post</title>
<link rel="stylesheet" href="https://fonts.googleapis.com/css2?family=Lato:wght@300;400;700;900&family=Roboto+Slab:wght@300;400&family=Noto+Serif:ital,wght@0,400;0,700;1,400&display=swap">
<style>
:root{
  --red:#f0401f;
  --teal:#2d4e58;
  --navy:#22404e;
  --ink:#222;
  --body:#444;
  --muted:#8a8a8a;
  --grey-panel:#ececec;
  --line:#e2e2e2;
  --green:#1fb89a;
}
*{box-sizing:border-box;margin:0;padding:0}
html,body{width:675px;height:1200px;overflow:hidden;background:#fff}
body{position:relative;font-family:'Lato',sans-serif;color:var(--body)}
.abs{position:absolute}

/* header */
.site-header{position:absolute;left:0;top:0;width:675px;height:83px;background:var(--teal);border-top:7px solid var(--red);border-bottom:2px solid var(--red)}
.brand{position:absolute;left:64px;top:20px;display:flex;align-items:center;gap:8px}
.brand-dot{width:16px;height:16px;border-radius:50%;background:var(--red)}
.brand-name{font-family:'Lato',sans-serif;font-weight:900;font-size:22px;color:#fff;letter-spacing:.2px;line-height:1}
.connect{position:absolute;right:63px;top:22px;display:flex;align-items:center;gap:6px;color:#fff;font-size:8px}
.connect span{margin-right:4px}
.social{width:16px;height:16px;border-radius:50%;background:#3f8fd4}
.social.alt{background:#e04a32}
.main-nav{position:absolute;right:60px;top:52px;display:flex;font-size:7.5px;font-weight:700;color:#fff}
.main-nav a{color:#fff;text-decoration:none}
.main-nav a.current{color:var(--red);font-weight:400}
.main-nav i{font-style:normal;margin:0 6px}

/* post */
.post-image{left:67px;top:97px;width:361px;height:197px;background:linear-gradient(180deg,#4b5a3a 0%,#5d6e3f 45%,#7d8a4a 70%,#6c7a3e 100%);border-bottom:3px solid var(--red)}
.post-date{left:70px;top:318px;width:32px;text-align:center;color:#9aa8b0}
.post-date .m{font-size:9px;font-weight:700;display:block}
.post-date .d{font-size:16px;display:block;line-height:1}
.date-rule{left:69px;top:358px;width:31px;height:1px;background:#c9d2d6}
.post-rule{left:107px;top:315px;width:1px;height:122px;background:#c9d2d6}
.post-title{left:115px;top:319px;font-size:12px;font-weight:400;color:var(--ink)}
.post-meta{left:116px;top:338px;font-size:5.5px;color:#aaa}
.post-body{left:116px;top:354px;width:312px;font-size:7.1px;line-height:12.7px;color:#444}

/* comments */
.avatar{border-radius:50%;background:linear-gradient(135deg,#3a4d63,#1d2a38)}
.comment-name{font-family:'Noto Serif',serif;font-size:8.5px;font-weight:700;color:var(--red)}
.comment-date{font-family:'Noto Serif',serif;font-size:8.5px;color:#888;margin-left:10px;font-weight:400}
.comment-text{font-family:'Noto Serif',serif;font-size:9px;line-height:12.75px;color:#333}

/* reply form */
.reply-title{left:92px;top:696px;font-family:'Roboto Slab',serif;font-weight:300;font-size:30px;color:var(--red)}
.reply-note{left:92px;top:746px;font-family:'Noto Serif',serif;font-size:8.5px;color:#888}
.field{left:92px;width:329px;height:24px;border:1px solid var(--line);border-radius:2px;display:flex;align-items:center;padding-left:8px;font-family:'Noto Serif',serif;font-size:8px;color:#888}
.field svg{width:9px;height:9px;margin-right:8px;stroke:#aaa;fill:none;stroke-width:1.2}
.field.area{align-items:flex-start;padding-top:8px}
.post-btn{left:92px;top:1039px;width:111px;height:25px;background:var(--red);border-radius:2px;color:#fff;font-size:8.5px;font-weight:900;letter-spacing:1.6px;display:flex;align-items:center;justify-content:center}

/* sidebar */
.search{left:449px;top:96px;width:170px;height:19px;border:1px solid var(--line)}
.search svg{position:absolute;right:5px;top:4px;width:10px;height:10px;stroke:#222;fill:none;stroke-width:1.6}
.widget-head{left:450px;width:173px;height:20px;background:var(--red);color:#fff;font-size:10.5px;display:flex;align-items:center;justify-content:center}
.news-panel{left:450px;top:147px;width:173px;height:185px;background:var(--grey-panel)}
.news-item{position:absolute;left:8px;width:158px;font-size:7.3px;line-height:10.6px;color:#555}
.read-more{display:block;text-align:right;color:var(--red);text-decoration:underline;margin-top:1px}
.ad{border:1px solid #ddd}
.recent-box{left:450px;top:578px;width:173px;height:217px;border:1px solid var(--line);border-top:none}
.recent-item{position:absolute;left:26px;width:118px;height:54px}
.recent-item .thumb{position:absolute;left:0;top:0;width:42px;height:41px}
.recent-item .date{position:absolute;left:53px;top:5px;font-family:'Noto Serif',serif;font-style:italic;font-size:5.8px;color:#aaa}
.recent-item .name{position:absolute;left:53px;top:16px;font-size:6px;font-weight:700;color:#333;line-height:8px}
.recent-item .cat{position:absolute;font-size:5.5px;font-weight:700;color:var(--green);left:53px}
.recent-item .sep{position:absolute;left:0;top:52px;width:118px;height:1px;background:var(--line)}

/* newsletter + footer */
.newsletter{left:0;top:1109px;width:675px;height:35px;background:var(--red)}
.newsletter h3{position:absolute;left:115px;top:7px;font-weight:300;font-size:16.5px;color:#fff}
.nl-input{position:absolute;left:266px;top:8px;width:198px;height:19px;background:#fff;font-size:8.5px;color:#333;padding:4px 10px}
.nl-submit{position:absolute;left:469px;top:8px;width:51px;height:19px;background:linear-gradient(#f4f4f4,#d9d9d9);border:1px solid #bbb;font-size:9px;color:#333;display:flex;align-items:center;justify-content:center}
.site-footer{left:0;top:1144px;width:675px;height:56px;background:var(--navy)}
.footer-nav{position:absolute;left:72px;top:22px;font-size:7.5px;color:#fff;display:flex}
.footer-nav i{font-style:normal;margin:0 6px}
.copyright{position:absolute;right:62px;top:21px;font-size:7.5px;color:#fff}
</style>
</head>
<body>

<header class="site-header">
  <div class="brand"><span class="brand-dot"></span><span class="brand-name">PathofthePlenty.com</span></div>
  <div class="connect"><span>Connect With us</span><i class="social"></i><i class="social"></i><i class="social"></i><i class="social alt"></i></div>
  <nav class="main-nav">
    <a class="current">Home</a><i>I</i><a>About</a><i>I</i><a>Blog</a><i>I</i><a>Start Here</a><i>I</i><a>Podcast</a><i>I</i><a>Ask Marvin</a><i>I</i><a>Resources</a>
  </nav>
</header>

<main>
  <div class="abs post-image" role="img" aria-label="Photo of sheep grazing in a green meadow before a line of trees"></div>
  <div class="abs post-date"><span class="m">APR</span><span class="d">22</span></div>
  <div class="abs date-rule"></div>
  <div class="abs post-rule"></div>
  <h1 class="abs post-title">The Quiet of the Meadow. Do you what version 1991 ?</h1>
  <div class="abs post-meta">Post by admin | Others | No Comments</div>
  <p class="abs post-body">People think focus means saying yes to the thing you've got to focus on. But that's not what it means at all. It means saying no to the hundred other good ideas that there are. You have to pick carefully. I'm actually as proud of the things we haven't done as the things I have done. Innovation is saying no to1,000 things. People think focus means saying yes to the thing you've got to focus . But that's not what it means at all. It means saying no to the hundred other good ideas that there are. You have to pick carefully. I'm actually as proud of the things we haven't done as the things I have done. Innovation is saying no to 1,000 things.</p>

  <div class="abs avatar" style="left:76px;top:481px;width:37px;height:37px" role="img" aria-label="Commenter avatar"></div>
  <div class="abs comment-name" style="left:124px;top:481px">Owen Marsh<span class="comment-date">April 3, 2015 at 9:08 am - Reply</span></div>
  <p class="abs comment-text" style="left:124px;top:506px;width:310px">Vestibulum vel lacus eu nunc euismod pharetra. Aliquam commodo, tellus ac hendrerit pellentesque, velit sem congue urna, id rutrum odio tortor eu mi.</p>

  <div class="abs avatar" style="left:67px;top:570px;width:38px;height:38px" role="img" aria-label="Commenter avatar"></div>
  <div class="abs comment-name" style="left:116px;top:570px">Colin Reed<span class="comment-date">April 3, 2015 at 9:08 am - Reply</span></div>
  <p class="abs comment-text" style="left:116px;top:595px;width:330px">Nulla sagittis fermentum leo ut mattis. Etiam congue velit quam, ut posuere nisl dignissim et. Nulla a ex at lectus tempor hendrerit. Fusce ligula diam, cursus eu interdum ac, volutpat at nibh. Nullam faucibus dolor ac neque venenatis, et rhoncus nibh commodo. Fusce ac ipsum dapibus, ultricies orci eu, imperdiet neque. Aenean justo libero, varius vel arcu vitae, molestie aliquet leo. Fusce tempor augue purus, eget venenatis nibh finibus eget. Ut magna lacus, porttitor sed erat sit amet, mattis maximus turpis.</p>

  <h2 class="abs reply-title">Leave a reply</h2>
  <p class="abs reply-note">Your email address will not be published. Required fields are marked *</p>
  <div class="abs field" style="top:782px"><svg viewBox="0 0 10 10"><circle cx="5" cy="3" r="2"/><path d="M1 9.5c0-2.5 8-2.5 8 0"/></svg>Name*</div>
  <div class="abs field" style="top:820px"><svg viewBox="0 0 10 10"><rect x="0.8" y="2" width="8.4" height="6"/><path d="M1 2.3l4 3 4-3"/></svg>Email*</div>
  <div class="abs field" style="top:862px"><svg viewBox="0 0 10 10"><circle cx="5" cy="5" r="4"/><path d="M1 5h8M5 1c-2 2.5-2 5.5 0 8M5 1c2 2.5 2 5.5 0 8"/></svg>Website</div>
  <div class="abs field area" style="top:901px;height:122px"><svg viewBox="0 0 10 10"><path d="M1.5 8.5l1-3 5-5 2 2-5 5z"/></svg>Comment*</div>
  <div class="abs post-btn">POST COMMENT</div>
</main>

<aside>
  <div class="abs search"><svg viewBox="0 0 10 10"><circle cx="4.2" cy="4.2" r="3.2"/><path d="M6.6 6.6l2.8 2.8"/></svg></div>
  <div class="abs widget-head" style="top:127px">Latest News</div>
  <div class="abs news-panel">
    <div class="news-item" style="top:5px">Test mauris tellus, ultricies quis hendrerit imper diet, faucibus non nulla. Curabitur congue dolor sed massa feugiat, sit amet tempor orci convalli s. Donec lacus magna<span class="read-more">Read More..</span></div>
    <div class="news-item" style="top:66px">Test mauris tellus, ultricies quis hendrerit imper diet, faucibus non nulla. Curabitur congue dolor sed massa feugiat<span class="read-more">Read More..</span></div>
    <div class="news-item" style="top:119px">Test mauris tellus, ultricies quis hendrerit imper diet, faucibus non nulla. Curabitur congue dolor sed massa feugiat, sit amet tempor orci convalli s. Donec lacus magna<span class="read-more">Read More..</span></div>
  </div>
  <div class="abs ad" style="left:450px;top:340px;width:174px;height:88px;background:linear-gradient(90deg,#d9a25a 0%,#f7f7f2 30%,#f7f7f2 70%,#c98a3c 100%)" role="img" aria-label="Advertisement banner for Spice Route restaurant with plates of food"></div>
  <div class="abs ad" style="left:451px;top:442px;width:173px;height:98px;background:linear-gradient(90deg,#b8404a 0%,#e8e4e2 40%,#eeeeee 100%)" role="img" aria-label="Advertisement banner for Lumiere Velvet Blush lipstick"></div>
  <div class="abs widget-head" style="top:558px;width:174px">Recent Post</div>
  <div class="abs recent-box">
    <div class="recent-item" style="top:17px">
      <div class="thumb" role="img" aria-label="Strawberry shortcake dessert photo" style="background:linear-gradient(135deg,#b96a6a,#e8d6c8)"></div>
      <span class="date">March 23, 2015</span><span class="name">STRAWBERRY<br>SHORTCAKE</span><span class="cat" style="top:37px">TRAVEL</span><i class="sep"></i>
    </div>
    <div class="recent-item" style="top:87px">
      <div class="thumb" role="img" aria-label="Photo of a person holding a rose" style="background:linear-gradient(135deg,#e98aa0,#f4e6e6)"></div>
      <span class="date">March 23, 2015</span><span class="name">GIRL WITH A ROSE</span><span class="cat" style="top:29px">FOOD</span><i class="sep"></i>
    </div>
    <div class="recent-item" style="top:150px">
      <div class="thumb" role="img" aria-label="Photo of a cat lying on the floor" style="background:linear-gradient(135deg,#8a6a52,#d8c6b0)"></div>
      <span class="date">March 23, 2015</span><span class="name">CAT ON THE FLOOR</span><span class="cat" style="top:29px">TRAVEL</span>
    </div>
  </div>
</aside>

<section class="abs newsletter">
  <h3>Join our Newsletter</h3>
  <div class="nl-input">E-mail adress</div>
  <div class="nl-submit">Submit</div>
</section>

<footer class="abs site-footer">
  <nav class="footer-nav"><span>Home</span><i>I</i><span>About</span><i>I</i><span>Blog</span><i>I</i><span>Start Here</span><i>I</i><span>Podcast</span><i>I</i><span>Ask Marvin</span><i>I</i><span>Resources</span></nav>
  <div class="copyright">©2015 by pathoftheplenty</div>
</footer>

</body>
</html>
```